Educational Flashcard Packaging Box Design

We are an educational resource provider in Australia. We have a new product launching for high school students, age 13-18. Thye are flashcards that help students with literacy. We need the box design that will store the cards when the students keep them in the bag at school. They need to be fun and colourful.
Our brand colours are
#06D8D8
#EF0081
#FFC904
#FF9900

The 36 flashcards all have a different colour to make up a rainbow. See the image of the flashcards attached.

The box template is uploaded in the files.
The box dimensions are 91 x 35 x 129mm.
Updates

I had a baby on the 2nd June and am in the hospital until the 8th June so I haven't been able to manage the project.

Target Market(s)

School students age 12 -18

Requirements
Must have
• Name of the product: Brightmark Mastery Flashcards
Fun and engaging design.
Bright colours.
Our logo - attached.
Text:
Get results you can be proud of.
36 flashcards + instructions
Increase key word knowledge and understanding.
(C) Harbourline Study Guild 2021
Newcastle, NSW, Australia.
hsguild.edu.au
Nice to have
• Instructions for the back of the box:
1. Box the key word in every question and check its meaning in the flashcards.
2. Write the meaning above the key word.
3. Use the key word metalanguage in your answer, e.g. describe; use the words characteristics and features in your answer. E.g. explain; use the words cause and effect in your answer and use linking words to demonstrate the relationships.
4. Be sure to add relevant example/s where possible

```html
<!DOCTYPE html>
<html lang="en">
<head>
<meta charset="utf-8">
<title>Brightmark Mastery Flashcards – Box Front</title>
<link rel="stylesheet" href="https://fonts.googleapis.com/css2?family=Montserrat:ital,wght@0,300;0,700;0,800;0,900;1,800;1,900&display=swap">
<style>
  :root{
    --bg:#dcdcdc;
    --teal:#06D8D8;
    --pink:#EF0081;
    --yellow:#FFC904;
    --orange:#FF9900;
    --rose:#f06aa8;
    --purple:#c45bd6;
    --lemon:#f2e24a;
    --amber:#f4b23c;
    --white:#ffffff;
    --ink:#1d1d1d;
  }
  *{box-sizing:border-box;margin:0;padding:0}
  html,body{width:1200px;height:1200px;overflow:hidden;background:var(--bg)}
  body{font-family:"Montserrat",sans-serif}
  .box-front{
    position:absolute;left:220px;top:61px;width:760px;height:1078px;
    background:var(--white);padding:26px;
    box-shadow:0 30px 60px rgba(0,0,0,.18);
  }
  .panel{position:relative;width:100%;height:100%;overflow:hidden;
    background:linear-gradient(180deg,
      var(--rose) 0 6%, var(--amber) 6% 12%, var(--lemon) 12% 22%,
      var(--teal) 22% 31%, var(--purple) 31% 38%, var(--rose) 38% 46%,
      var(--amber) 46% 53%, var(--lemon) 53% 63%, var(--teal) 63% 72%,
      var(--purple) 72% 80%, var(--rose) 80% 88%, var(--pink) 88% 100%);
  }
  .title{position:absolute;top:64px;left:0;right:0;text-align:center;z-index:2}
  .title-main{font-weight:900;font-style:italic;font-size:50px;color:var(--white);
    letter-spacing:.5px;text-shadow:0 3px 0 rgba(0,0,0,.12)}
  .title-sub{display:inline-block;margin-top:6px;padding:6px 26px;
    background:linear-gradient(90deg,var(--teal),#7fe9c9);border:3px solid var(--white);
    font-weight:300;font-size:26px;letter-spacing:12px;color:var(--white)}
  .tagline{position:absolute;top:278px;left:40px;right:40px;text-align:center;line-height:1.05;z-index:2}
  .tagline .strong{display:block;font-weight:900;font-style:italic;font-size:56px;color:var(--yellow);
    text-shadow:0 3px 0 rgba(0,0,0,.12)}
  .tagline .light{display:block;font-weight:300;font-size:52px;color:var(--white)}
  .brand{position:absolute;left:64px;top:640px;display:flex;align-items:center;gap:14px;z-index:2}
  .brand-mark{width:40px;height:40px;border:5px solid var(--ink)}
  .brand-name{font-weight:800;font-size:24px;color:var(--ink);line-height:1.1;width:190px}
  .card-fan{position:absolute;right:-40px;top:520px;width:340px;height:330px;
    transform:rotate(-14deg);border-radius:18px;z-index:1;
    background:linear-gradient(135deg,#fbf1a8 0%,#fff07a 40%,#d27ee0 75%,#f26b6b 100%)}
  .count-badge{position:absolute;left:46px;top:860px;display:flex;align-items:center;gap:12px;z-index:2;
    background:var(--yellow);border-radius:10px;padding:8px 18px 8px 10px;transform:rotate(6deg)}
  .count-num{background:var(--teal);color:var(--white);font-weight:900;font-size:40px;
    padding:2px 12px;border-radius:8px;border:3px solid var(--white)}
  .count-text{font-weight:800;font-style:italic;font-size:19px;color:var(--ink);line-height:1.05}
  .footer-line{position:absolute;left:0;right:0;bottom:34px;text-align:center;z-index:2;
    font-weight:700;font-size:17px;color:var(--white);letter-spacing:.3px}
</style>
</head>
<body>
  <main class="box-front">
    <section class="panel">
      <header class="title">
        <h1 class="title-main">BRIGHTMARK MASTERY</h1>
        <div class="title-sub">FLASHCARDS</div>
      </header>

      <p class="tagline">
        <span class="strong">GET RESULTS</span>
        <span class="light">YOU CAN BE</span>
        <span class="strong">PROUD OF</span>
      </p>

      <div class="brand">
        <span class="brand-mark"></span>
        <span class="brand-name">Harbourline Study Guild</span>
      </div>

      <div class="card-fan" role="img" aria-label="Illustration of a fanned stack of colourful key word flashcards"></div>

      <div class="count-badge">
        <span class="count-num">36</span>
        <span class="count-text">FLASHCARDS<br>+ INSTRUCTIONS</span>
      </div>

      <p class="footer-line">INCREASE KEY WORD KNOWLEDGE AND UNDERSTANDING.</p>
    </section>
  </main>
</body>
</html>
```